Letterhead

Can you please design me a letterhead that I can use electronically in word as a template. I have attached my business card as I would like the design to reflect this logo.

```html
<!DOCTYPE html>
<html lang="en">
<head>
<meta charset="utf-8">
<title>Kestrel Letterhead</title>
<link rel="stylesheet" href="https://fonts.googleapis.com/css2?family=Open+Sans:wght@400;600&display=swap">
<style>
  :root {
    --brand-red: #c00000;
    --ink-black: #111111;
    --text-grey: #4a4a4a;
    --paper: #ffffff;
    --backdrop: #e4e6ea;
  }
  * { margin: 0; padding: 0; box-sizing: border-box; }
  html, body {
    width: 1200px;
    height: 1156px;
    overflow: hidden;
    background: var(--backdrop);
  }
  .letterhead {
    position: absolute;
    left: 163px;
    top: 0;
    width: 874px;
    height: 1156px;
    background: var(--paper);
    font-family: "Open Sans", Arial, sans-serif;
  }
  .top-band-black {
    position: absolute; left: 0; top: 0;
    width: 669px; height: 11px;
    background: var(--ink-black);
  }
  .top-band-red {
    position: absolute; left: 669px; top: 0;
    width: 205px; height: 13px;
    background: var(--brand-red);
  }
  .company {
    position: absolute; left: 70px; top: 56px;
    display: flex; align-items: center; gap: 14px;
  }
  .company-mark {
    width: 24px; height: 24px;
    background: var(--brand-red);
    flex: none;
  }
  .company-name {
    font-size: 20px; font-weight: 600; line-height: 26px;
    color: var(--brand-red);
  }
  .contact {
    position: absolute; left: 382px; top: 64px;
    color: var(--text-grey);
  }
  .contact .name-line {
    font-size: 14px; font-weight: 600; line-height: 20px;
  }
  .contact .detail-line {
    font-size: 11px; line-height: 18px;
  }
  .role { color: var(--brand-red); font-weight: 400; }
  .divider { color: var(--brand-red); padding: 0 3px; }
  .label { color: var(--brand-red); font-weight: 600; }
  .bottom-band-red {
    position: absolute; left: 0; bottom: 0;
    width: 664px; height: 44px;
    background: var(--brand-red);
  }
  .bottom-band-black {
    position: absolute; left: 664px; bottom: 0;
    width: 210px; height: 44px;
    background: var(--ink-black);
  }
</style>
</head>
<body>
  <main class="letterhead">
    <div class="top-band-black"></div>
    <div class="top-band-red"></div>

    <div class="company">
      <div class="company-mark"></div>
      <p class="company-name">Kestrel Business<br>Consultants Pty Ltd</p>
    </div>

    <div class="contact">
      <p class="name-line">Maren Whitfield<span class="divider">|</span><span class="role">Principal</span></p>
      <p class="detail-line"><span class="label">P</span> : 0400 555 182<span class="divider">|</span><span class="label">E</span> : maren@kestrelbc.example<span class="divider">|</span><span class="label">ACN</span> : 000 123 456</p>
    </div>

    <div class="bottom-band-red"></div>
    <div class="bottom-band-black"></div>
  </main>
</body>
</html>
```